Quorlify Business Card

We require a stunning business card for Quorlify - a new digital marketing agency. The logo provided was designed by a graphic designer here on Artboxly.

www.quorlify-example.com - "Get more sales online"

What we do:
The business delivers website optimisation (Web design, social media strategy, digital strategies, SEO, PPC, conversion optimisation, email marketing) to get businesses more sales online.

The card must match the brand style which can be found on this website template:

http://layoutmarket.example/item/brightline-adaptive-versatile-layout/full_screen_preview/9137462

It must have 'wow' factor so that you'll never forget Quorlify - We're open to any materials, textures you think will work.

We don't want a boring run of the mill design - I can knock that up in Photoshop myself or use a template solution. It should be timeless and only need replacing should the contact details change.

The design should be eye catching, future proof, exceptionally chic, classy and oozing authority and confidence. Quorlify services must not look cheap.

Here's some brilliant designs to point you in the right direction:

http://tidyprints.example/30-remarkable-calling-cards/

The spec is for double sided, but we're open to your ideas. If it's going on an opaque or see through card, then of course a single side is preferable. Using creativity and thought on the medium for the card - shape - texture is desirable.

The strapline for the business is "Get more business online" please submit with / without strapline.
Updates

Please only submit your best 1-3 designs initially.

Target Market(s)

Business 2 Business - Local SMEs
Local professionals - Doctors, Dentists, Financials, Bespoke Retailers, Property companies - anyone with a decent budget to spend on digital marketing services and a high margin product or service to sell.

Industry/Entity Type

Graphic Designer

Requirements
Must have
• Text:
• name: Tom Vandlow
• position Digital Marketing Director
• mobile 07951 238 604
• website www.quorlify-example.com
Nice to have
• Check See http://tidyprints.example/30-remarkable-calling-cards/ for ideas.
• LinkedIn and Twitter usernames if there is space and it works on the design.

```html
<!DOCTYPE html>
<html lang="en">
<head>
<meta charset="UTF-8">
<title>Quorlify Business Card</title>
<link href="https://fonts.googleapis.com/css2?family=Titillium+Web:wght@400;600;700&display=swap" rel="stylesheet">
<style>
  :root {
    --page: #ffffff;
    --charcoal: #353535;
    --charcoal-deep: #2b2b2b;
    --coral: #ee4135;
    --white: #ffffff;
    --stone: #e8e8e8;
    --stone-dark: #dcdcdc;
    --grey-text: #6b6b6b;
  }
  * { box-sizing: border-box; margin: 0; padding: 0; }
  html, body {
    width: 959px; height: 1200px; overflow: hidden;
    background: var(--page);
    font-family: "Titillium Web", sans-serif;
  }
  .canvas { position: relative; width: 959px; height: 1200px; }
  .card { position: absolute; left: 24px; width: 910px; height: 567px; overflow: hidden; }

  /* Front */
  .card--front {
    top: 20px;
    background: radial-gradient(ellipse at 50% 40%, var(--charcoal) 0%, var(--charcoal-deep) 100%);
  }
  .brand-mark {
    position: absolute; left: 92px; top: 165px;
    width: 140px; height: 140px; border-radius: 50%;
    background: var(--coral);
  }
  .brand-name {
    position: absolute; right: 90px; top: 175px;
    font-size: 150px; font-weight: 700; line-height: 1;
    color: var(--white); letter-spacing: -1px;
  }
  .brand-url {
    position: absolute; right: 90px; top: 388px;
    font-size: 23px; font-weight: 400; color: var(--white); letter-spacing: 0.5px;
  }
  .services {
    position: absolute; right: 25px; top: 490px;
    font-size: 25px; font-weight: 400; color: var(--white); white-space: nowrap;
  }
  .services .sep { margin: 0 8px; }
  .services-rule {
    position: absolute; left: 353px; right: 0; top: 527px; height: 7px;
    background: var(--coral); border-radius: 4px 0 0 4px;
  }

  /* Back */
  .card--back {
    top: 609px;
    background: radial-gradient(ellipse at 30% 30%, var(--stone) 0%, var(--stone-dark) 100%);
  }
  .person {
    position: absolute; left: 30px; top: 222px; width: 375px;
  }
  .person-name {
    font-size: 68px; font-weight: 400; line-height: 1; color: var(--coral);
    white-space: nowrap;
  }
  .person-role {
    margin-top: 14px; text-align: right;
    font-size: 17px; font-weight: 600; color: var(--grey-text);
    letter-spacing: 2.5px; text-transform: uppercase; white-space: nowrap;
  }
  .contact-list { position: absolute; left: 425px; top: 112px; list-style: none; }
  .contact-item { display: flex; height: 50px; margin-bottom: 8.5px; }
  .contact-icon {
    width: 50px; height: 50px; background: var(--coral);
    display: flex; align-items: center; justify-content: center;
  }
  .contact-icon svg { width: 36px; height: 36px; }
  .contact-label {
    margin-left: 7px; height: 50px; padding: 0 18px;
    background: var(--coral); color: var(--white);
    font-size: 27px; font-weight: 400; line-height: 50px; white-space: nowrap;
  }
</style>
</head>
<body>
<div class="canvas">

  <section class="card card--front">
    <div class="brand-mark"></div>
    <div class="brand-name">Quorlify</div>
    <div class="brand-url">www.quorlify-example.com</div>
    <div class="services">Web Design<span class="sep">|</span>SEO<span class="sep">|</span>PPC<span class="sep">|</span>Email Marketing</div>
    <div class="services-rule"></div>
  </section>

  <section class="card card--back">
    <div class="person">
      <div class="person-name">Tom Vandlow</div>
      <div class="person-role">Digital Marketing Director</div>
    </div>

    <ul class="contact-list">
      <li class="contact-item">
        <span class="contact-icon">
          <svg viewBox="0 0 36 36"><path d="M18 3a10 10 0 0 0-10 10c0 8 10 20 10 20s10-12 10-20A10 10 0 0 0 18 3z" fill="#fff"/><circle cx="18" cy="13" r="4" fill="#ee4135"/></svg>
        </span>
        <span class="contact-label">My place, my town, my city</span>
      </li>
      <li class="contact-item">
        <span class="contact-icon">
          <svg viewBox="0 0 36 36" fill="none" stroke="#fff" stroke-width="2"><rect x="3" y="8" width="30" height="20"/><path d="M3 8l15 12 15-12M3 28l11-10M33 28l-11-10"/></svg>
        </span>
        <span class="contact-label">www.quorlify-example.com</span>
      </li>
      <li class="contact-item">
        <span class="contact-icon">
          <svg viewBox="0 0 36 36" fill="none" stroke="#fff" stroke-width="2"><circle cx="18" cy="18" r="14"/><ellipse cx="18" cy="18" rx="6" ry="14"/><path d="M4 18h28M6 11h24M6 25h24M18 4v28"/></svg>
        </span>
        <span class="contact-label">myemail@quorlify-example.com</span>
      </li>
      <li class="contact-item">
        <span class="contact-icon">
          <svg viewBox="0 0 36 36"><rect x="3" y="3" width="30" height="30" rx="7" fill="#fff"/><path d="M13 9l4 5-2 3c1 3 3 5 6 6l3-2 5 4-2 3c-8 0-16-8-16-16z" fill="#ee4135"/></svg>
        </span>
        <span class="contact-label">07951 238 604</span>
      </li>
      <li class="contact-item">
        <span class="contact-icon">
          <svg viewBox="0 0 36 36"><circle cx="18" cy="18" r="11" fill="#fff"/></svg>
        </span>
        <span class="contact-label">chatterline.example/quorlify</span>
      </li>
      <li class="contact-item">
        <span class="contact-icon">
          <svg viewBox="0 0 36 36"><rect x="7" y="7" width="22" height="22" fill="#fff"/></svg>
        </span>
        <span class="contact-label">proflink.example/quorlify</span>
      </li>
    </ul>
  </section>

</div>
</body>
</html>
```